business card with 2 locations on 1 card

I need a modern looking business card that I would use at 2 different locations. Possibly 1 location on 1 side and other location on other side. One should be able to distinguish the 2 locations immediately before having to read the address or description on card. You can take a look at my website to see what I'm drawn to. The logo is brand new that I just purchased on Craft Hive. I want to emphasize family.
Updates

Let's not use the yellow and blue colors. Added Thursday, August 31, 2017

Target Market(s)

women and children

Industry/Entity Type

Health And Wellness

Contact Information for Business Card

Business name: Willow Brook Chiropractic & Acupuncture
My name: Lorin Daske
Job title: DC, MAOM, LAc (CA), CNS

Location 1
Address: 4817 Marlowe Blvd, Suite B-100, Frisco, TX 75034
Phone: (469) 555-0182
Fax: (972) 555-0137

Location 2
Address: 1936 Belvane Road, Suite 100, Plano, TX 75075
Phone: (469) 555-0169
Fax: (972) 555-0137

Email: drlorindaske@mailnest.example
Website: www.drlorindaske.example

Font styles to use
Serif
Sans Serif

Colors

Designer to choose colors to be used in the design.

Requirements
Must have
• distinction between 2 locations.
Nice to have
• Colors preference below is there. But I like to see what you come up with too!

```html
<!DOCTYPE html>
<html lang="en">
<head>
<meta charset="utf-8">
<title>Willow Brook Chiropractic &amp; Acupuncture – Business Card</title>
<link rel="stylesheet" href="https://fonts.googleapis.com/css2?family=Noto+Serif:wght@400;700&family=Courgette&display=swap">
<style>
  :root {
    --backdrop: #111111;
    --teal: #2a7370;
    --teal-deep: #236563;
    --green: #b4d46a;
    --paper: #ffffff;
    --ink: #222222;
    --shadow: rgba(0,0,0,0.55);
  }
  * { box-sizing: border-box; margin: 0; padding: 0; }
  html, body { width: 1200px; height: 1000px; overflow: hidden; background: var(--backdrop); }
  body { position: relative; font-family: "Noto Serif", Georgia, serif; color: var(--ink); }

  .card {
    position: absolute;
    width: 520px;
    height: 297px;
    box-shadow: 0 14px 30px var(--shadow);
    overflow: hidden;
  }

  /* Back side */
  .card-back { left: 70px; top: 170px; background: var(--teal); }
  .card-back .leaf-field {
    position: absolute; inset: 0;
    background: radial-gradient(circle at 40% 50%, #2f7d79 0%, var(--teal) 55%, var(--teal-deep) 100%);
  }
  .card-back .brand {
    position: absolute; left: 0; right: 0; top: 50%;
    transform: translateY(-50%);
    display: flex; flex-direction: column; align-items: center; gap: 14px;
  }
  .brand-dot { width: 90px; height: 90px; border-radius: 50%; background: var(--paper); }
  .brand-name-back { color: var(--paper); font-size: 22px; font-weight: 700; letter-spacing: 1px; }

  /* Front side */
  .card-front { left: 610px; top: 480px; background: var(--paper); }
  .person { position: absolute; left: 30px; top: 22px; }
  .person-name { font-family: "Courgette", cursive; color: var(--teal); font-size: 32px; line-height: 1.1; }
  .person-title { font-size: 12px; font-weight: 700; margin-top: 2px; }
  .contact-lines { margin-top: 8px; font-size: 11px; line-height: 1.45; }
  .contact-lines li { list-style: none; display: flex; align-items: center; gap: 6px; }
  .icon { width: 11px; height: 11px; flex: none; }

  .location { position: absolute; display: flex; align-items: center; gap: 10px; font-size: 12px; line-height: 1.3; }
  .location-frisco { left: 0; top: 148px; width: 290px; height: 50px; background: var(--green); padding-left: 22px; color: var(--ink); }
  .location-plano { left: 290px; top: 198px; width: 230px; height: 50px; background: var(--teal); padding-left: 16px; color: var(--paper); }
  .pin { width: 16px; height: 22px; flex: none; }

  .phone { position: absolute; display: flex; align-items: center; gap: 7px; font-size: 12px; font-weight: 700; }
  .phone-frisco { left: 26px; top: 218px; }
  .fax-shared { left: 160px; top: 218px; }
  .phone-plano { left: 330px; top: 264px; }

  .brand-front { position: absolute; left: 320px; top: 96px; width: 190px; display: flex; align-items: center; gap: 10px; }
  .brand-front .brand-dot { width: 44px; height: 44px; background: var(--teal); flex: none; }
  .brand-name-front { color: var(--teal); font-size: 13px; font-weight: 700; line-height: 1.2; }
</style>
</head>
<body>

  <section class="card card-back" aria-label="Card back">
    <div class="leaf-field" role="img" aria-label="Soft teal field of scattered leaf shapes"></div>
    <div class="brand">
      <span class="brand-dot"></span>
      <span class="brand-name-back">Willow Brook</span>
    </div>
  </section>

  <section class="card card-front" aria-label="Card front">
    <div class="person">
      <h1 class="person-name">Lorin Daske</h1>
      <p class="person-title">DC, MAOM, LAc (CA), CNS</p>
      <ul class="contact-lines">
        <li>
          <svg class="icon" viewBox="0 0 12 12"><rect x="0.5" y="2" width="11" height="8" fill="var(--teal)"/><path d="M0.5 2 L6 7 L11.5 2" stroke="#fff" fill="none"/></svg>
          drlorindaske@mailnest.example
        </li>
        <li>
          <svg class="icon" viewBox="0 0 12 12"><circle cx="6" cy="6" r="5.2" fill="none" stroke="var(--teal)" stroke-width="1.2"/><path d="M1 6 H11 M6 1 C3 4 3 8 6 11 M6 1 C9 4 9 8 6 11" stroke="var(--teal)" fill="none"/></svg>
          www.drlorindaske.example
        </li>
      </ul>
    </div>

    <div class="location location-frisco">
      <svg class="pin" viewBox="0 0 16 22"><path d="M8 0 C3.6 0 0 3.5 0 8 C0 14 8 22 8 22 C8 22 16 14 16 8 C16 3.5 12.4 0 8 0 Z" fill="var(--teal)"/><circle cx="8" cy="8" r="3" fill="var(--green)"/></svg>
      <address style="font-style:normal">4817 Marlowe Blvd<br>Suite B-100, Frisco, TX 75034</address>
    </div>

    <div class="location location-plano">
      <svg class="pin" viewBox="0 0 16 22"><path d="M8 0 C3.6 0 0 3.5 0 8 C0 14 8 22 8 22 C8 22 16 14 16 8 C16 3.5 12.4 0 8 0 Z" fill="var(--green)"/><circle cx="8" cy="8" r="3" fill="var(--teal)"/></svg>
      <address style="font-style:normal">1936 Belvane Road, Suite 100<br>Plano, TX 75075</address>
    </div>

    <div class="brand-front">
      <span class="brand-dot"></span>
      <span class="brand-name-front">Willow Brook Chiropractic &amp; Acupuncture</span>
    </div>

    <p class="phone phone-frisco">
      <svg class="icon" viewBox="0 0 12 12"><path d="M3 1 L5 3.5 L4 5 C4.8 6.8 5.8 7.8 7 8.3 L8.5 7.3 L11 9.3 L9.5 11 C5 10.5 1.5 7 1 2.5 Z" fill="var(--teal)"/></svg>
      (469) 555-0182
    </p>
    <p class="phone fax-shared">
      <svg class="icon" viewBox="0 0 12 12"><rect x="1" y="4" width="10" height="6" fill="var(--teal)"/><rect x="3" y="1" width="6" height="3" fill="var(--teal)"/><rect x="3" y="6" width="6" height="1" fill="#fff"/></svg>
      (972) 555-0137
    </p>
    <p class="phone phone-plano">
      <svg class="icon" viewBox="0 0 12 12"><path d="M3 1 L5 3.5 L4 5 C4.8 6.8 5.8 7.8 7 8.3 L8.5 7.3 L11 9.3 L9.5 11 C5 10.5 1.5 7 1 2.5 Z" fill="var(--teal)"/></svg>
      (469) 555-0169
    </p>
  </section>

</body>
</html>
```